Fahrzeugbeschriftung für Elektrofirma
Zielgruppe
Wir sind eine Elektrofirma und suchen ein hochwertiges Design, unsere Ziehlgruppe sind smarthome bewuste Familen oder Männner.
Aufgabenstellung
Wir haben varelle Toriv L1 H2 und vastrano L1 H2,
So ähnlich wie bei Lutz & Baier
Hinten: - Gebäudetechnik , - Smarthome, - Sicherheitstechnik,
Telefonnummer 02087 3519284
Facebook: ElektroTannreuter
Instagram: elektro_tannreuter
Seiten: Ahornweg 17
47128 Dinslaken
Seiten hinten: Logo mit Tannreuter Elektro- und Datentechnik
www.elektro-tannreuter-beispiel.de, info@elektro-tannreuter-beispiel.de
keine komplett Folierung

```html
<!DOCTYPE html>
<html lang="de">
<head>
<meta charset="utf-8">
<title>Tannreuter Elektro- und Datentechnik – Fahrzeugbeschriftung Seite</title>
<link rel="stylesheet" href="https://fonts.googleapis.com/css2?family=Montserrat:wght@500;600&family=Roboto:wght@400;500&display=swap">
<style>
  :root {
    --navy: #1c2b4c;
    --navy-light: #2a3d66;
    --teal: #2ba4ad;
    --white: #ffffff;
    --page: #f4f5f7;
    --panel-edge: #d9dde3;
    --text-dark: #1c2b4c;
  }
  html, body {
    margin: 0;
    padding: 0;
    width: 1200px;
    height: 800px;
    overflow: hidden;
    background: var(--page);
  }
  .canvas {
    position: relative;
    width: 1200px;
    height: 800px;
  }
  .livery {
    position: absolute;
    left: 40px;
    top: 180px;
    width: 1120px;
    height: 440px;
    background: var(--white);
    border: 1px solid var(--panel-edge);
    border-radius: 18px;
    overflow: hidden;
  }
  .livery__band {
    position: absolute;
    inset: 0;
    width: 100%;
    height: 100%;
  }
  .brand {
    position: absolute;
    left: 120px;
    top: 30px;
    display: flex;
    align-items: center;
    gap: 22px;
  }
  .brand__dot {
    width: 92px;
    height: 92px;
    border-radius: 50%;
    background: var(--teal);
    flex: none;
  }
  .brand__name {
    font-family: "Montserrat", sans-serif;
    font-weight: 600;
    font-size: 56px;
    letter-spacing: 4px;
    color: var(--navy);
    line-height: 1;
  }
  .brand__tagline {
    font-family: "Montserrat", sans-serif;
    font-weight: 500;
    font-size: 24px;
    letter-spacing: 1px;
    color: var(--teal);
    text-transform: uppercase;
    margin-top: 6px;
  }
  .services {
    position: absolute;
    left: 318px;
    top: 136px;
    font-family: "Roboto", sans-serif;
    font-weight: 500;
    font-size: 17px;
    line-height: 20px;
    color: var(--navy);
    display: flex;
    gap: 26px;
  }
  .contact {
    position: absolute;
    font-family: "Roboto", sans-serif;
    display: flex;
    align-items: center;
    gap: 10px;
  }
  .contact svg { flex: none; }
  .contact--phone {
    left: 300px;
    top: 240px;
    font-size: 34px;
    font-weight: 500;
    color: var(--white);
    letter-spacing: 1px;
  }
  .contact--address {
    left: 640px;
    top: 190px;
    font-size: 18px;
    line-height: 22px;
    font-weight: 500;
    color: var(--text-dark);
    transform: rotate(9.13deg);
    transform-origin: left bottom;
  }
  .contact--web,
  .contact--mail {
    top: 360px;
    font-size: 19px;
    font-weight: 500;
    color: var(--white);
  }
  .contact--web { left: 360px; }
  .contact--mail { left: 700px; }
</style>
</head>
<body>
<main class="canvas">
  <section class="livery" aria-label="Fahrzeugbeschriftung Seitenansicht">
    <svg class="livery__band" viewBox="0 0 1120 440" preserveAspectRatio="none" aria-hidden="true">
      <polygon points="0,120 1120,300 1120,440 0,440" fill="var(--navy)"/>
      <polygon points="0,120 1120,300 1120,306 0,126" fill="var(--navy-light)"/>
    </svg>

    <div class="brand">
      <div class="brand__dot"></div>
      <div>
        <div class="brand__name">TANNREUTER</div>
        <div class="brand__tagline">Elektro- und Datentechnik</div>
      </div>
    </div>

    <div class="services">
      <span>Smarthome</span>
      <span>Haustechnik</span>
      <span>Sicherheitstechnik</span>
    </div>

    <div class="contact contact--phone">
      <svg width="26" height="26" viewBox="0 0 24 24" aria-hidden="true">
        <circle cx="12" cy="12" r="12" fill="var(--white)"/>
        <path d="M8.2 6.5l1.6-.4 1.2 2.8-1.2.9a7 7 0 0 0 3.3 3.3l.9-1.2 2.8 1.2-.4 1.6c-.2.6-.8 1-1.4.9A9.5 9.5 0 0 1 7.3 7.9c-.1-.6.3-1.2.9-1.4z" fill="var(--navy)"/>
      </svg>
      <span>02087/3519284</span>
    </div>

    <div class="contact contact--address">
      <span>Ahornweg 17, 47128 Dinslaken</span>
    </div>

    <div class="contact contact--web">
      <svg width="20" height="20" viewBox="0 0 24 24" aria-hidden="true">
        <circle cx="12" cy="12" r="11" fill="var(--white)"/>
        <circle cx="12" cy="12" r="6.5" fill="none" stroke="var(--navy)" stroke-width="1.6"/>
        <path d="M5.5 12h13M12 5.5c2.5 2.5 2.5 10.5 0 13M12 5.5c-2.5 2.5-2.5 10.5 0 13" fill="none" stroke="var(--navy)" stroke-width="1.4"/>
      </svg>
      <span>www.elektro-tannreuter-beispiel.de</span>
    </div>

    <div class="contact contact--mail">
      <svg width="20" height="20" viewBox="0 0 24 24" aria-hidden="true">
        <circle cx="12" cy="12" r="11" fill="var(--white)"/>
        <rect x="6" y="8" width="12" height="8.5" rx="1" fill="none" stroke="var(--navy)" stroke-width="1.6"/>
        <path d="M6.5 8.7l5.5 4.2 5.5-4.2" fill="none" stroke="var(--navy)" stroke-width="1.5"/>
      </svg>
      <span>info@elektro-tannreuter-beispiel.de</span>
    </div>
  </section>
</main>
</body>
</html>
```